Business card design needed

Card needs to show Currency trading and strategic solutions for businesses and investing. Need a variety of currency symbols in the design ie pound, Euro, dollar, Yen. Like the idea of jigsaw puzzle pieces. Theme of building wealth and investments. Like purple, black and grey. Based in Queensland, Australia.
Updates

Thank you for all your designs.  We'll be making a decision soon. Cheers

Industry/Entity Type

Building

Contact Information for Business Card

Tulip Ridge Investments,
Email: tulipridgeinvestmens@quellmail.com.au,
Company Director - Maren Dusk
Senior Strategic Advisor - Owen Dusk
0437259604

```html
<!DOCTYPE html>
<html lang="en">
<head>
<meta charset="utf-8">
<title>Tulip Ridge Investments – Business Card</title>
<link rel="stylesheet" href="https://fonts.googleapis.com/css2?family=Cinzel:wght@600&family=Open+Sans:wght@300&family=Archivo+Black&family=Kaushan+Script&family=Inconsolata:wght@400&display=swap">
<style>
  :root {
    --card-bg: #231f20;
    --band-grey: #2e2d2e;
    --band-block: #343334;
    --band-purple: #7b6579;
    --puzzle-light: #a98aaa;
    --puzzle-mid: #6a2a66;
    --puzzle-dark: #3a1a38;
    --text-white: #ffffff;
  }
  * { margin: 0; padding: 0; box-sizing: border-box; }
  html, body { width: 1200px; height: 694px; overflow: hidden; background: var(--card-bg); }
  .card { position: relative; width: 1200px; height: 694px; background: var(--card-bg); color: var(--text-white); overflow: hidden; }

  .band { position: absolute; top: 0; height: 694px; width: 71px; }
  .band--grey-left { left: 82px; background: var(--band-grey); }
  .band--grey-right { left: 304px; background: var(--band-grey); }
  .band--purple { left: 198px; width: 70px; background: var(--band-purple); }
  .band-block { position: absolute; left: 82px; top: 145px; width: 293px; height: 172px; background: var(--card-bg); }
  .band-block__inner { position: absolute; left: 0; top: 55px; width: 293px; height: 108px; background: var(--band-block); }

  .brand { position: absolute; left: 82px; top: 198px; width: 293px; text-align: center;
    font-family: "Cinzel", serif; font-weight: 600; font-size: 27px; line-height: 38px; color: var(--text-white); }

  .puzzle-art { position: absolute; left: 740px; top: 64px; width: 392px; height: 226px; }

  .tagline { position: absolute; left: 380px; top: 236px; width: 700px; text-align: center;
    font-family: "Open Sans", sans-serif; font-weight: 300; font-size: 49px; line-height: 67px; white-space: nowrap; }

  .phone { position: absolute; left: 378px; top: 452px; width: 700px; text-align: center;
    font-family: "Archivo Black", sans-serif; font-size: 33px; letter-spacing: 3px; line-height: 38px; white-space: nowrap; }
  .email { position: absolute; left: 328px; top: 485px; width: 800px; text-align: center;
    font-family: "Archivo Black", sans-serif; font-size: 24px; letter-spacing: 0.6px; line-height: 30px; white-space: nowrap; }

  .person { position: absolute; top: 530px; text-align: center; white-space: nowrap; }
  .person--director { left: 400px; width: 310px; }
  .person--advisor { left: 720px; width: 310px; }
  .person__name { font-family: "Kaushan Script", cursive; font-size: 50px; line-height: 66px; }
  .person__role { font-family: "Inconsolata", monospace; font-size: 20px; letter-spacing: 1.2px; line-height: 24px; }
</style>
</head>
<body>
  <main class="card">
    <div class="band band--grey-left"></div>
    <div class="band band--purple"></div>
    <div class="band band--grey-right"></div>
    <div class="band-block"><div class="band-block__inner"></div></div>

    <div class="brand">TULIP RIDGE<br>INVESTMENTS</div>

    <svg class="puzzle-art" viewBox="0 0 392 226" role="img" aria-label="Jigsaw puzzle pieces carrying dollar, euro, yen and pound symbols">
      <defs>
        <linearGradient id="puzzle-tone" x1="0" y1="0" x2="1" y2="1">
          <stop offset="0" stop-color="var(--puzzle-light)"/>
          <stop offset="0.5" stop-color="var(--puzzle-mid)"/>
          <stop offset="1" stop-color="var(--puzzle-dark)"/>
        </linearGradient>
      </defs>
      <path d="M10 50 L110 30 L150 120 L140 178 L20 178 Z" fill="var(--puzzle-light)"/>
      <path d="M160 4 H388 V222 H248 V116 H160 Z" fill="url(#puzzle-tone)"/>
    </svg>

    <h1 class="tagline">Currency Trading<br>and<br>Investment Strategies</h1>

    <p class="phone">0437 259 604</p>
    <p class="email">tulipridgeinvestmens@quellmail.com.au</p>

    <div class="person person--director">
      <p class="person__name">Maren Dusk</p>
      <p class="person__role">Company Director</p>
    </div>
    <div class="person person--advisor">
      <p class="person__name">Owen Dusk</p>
      <p class="person__role">Senior Strategic Advisor</p>
    </div>
  </main>
</body>
</html>
```